New Bottle Label for our Velmoris Grand Reserva Brandy

Graphic Design Brief
We need a new bottle label for our Brandy Gran Reserva that we want to bring to the market.
Please have a look at all our current bottles and labels and the feel of our company under www.velmoris-distill.ch. We would like the design to be still different to the rest - as it is not a whisky, not a fruit product, not a spirit like a gin, thus we need to create like a new family, but still fitting in with the rest of the products.
The bottle that we will be using for the brand is a different one than the one that we already have, the design of the bottle is attached with a document.
I have also attached a briefing in regards to Brandy in general for your information.
### 1. What is Brandy?
Brandy is a distilled spirit made from fermented wine or other fruit wines. It is traditionally aged in oak barrels, which gives it its characteristic color and rich flavor. The aging process in oak is essential for developing the aromas and quality of the brandy.
### 2. What is Brandy Reserva?
A Brandy labeled as "Reserva" has undergone a longer aging process, typically at least 2 to 3 years, in oak barrels. This aging gives the brandy a deeper, more complex flavor profile and a darker color. "Reserva" is often an indication of higher quality.
### 3. Who enjoys drinking Brandy?
Brandy is typically favored by those who appreciate a deep, rich tasting experience. This often includes older consumers who value the time-aged complexity of the spirit. However, Brandy is also gaining popularity among younger people, especially through cocktails and modern serving styles.
### 4. Why is Brandy trending?
Brandy is experiencing a resurgence as consumers increasingly value quality and artisanal production methods. Its versatility in cocktails and association with traditional, luxurious experiences have also contributed to its renewed popularity.
### 5. What colors would be associated with Brandy?
The typical colors associated with Brandy are warm gold, amber, and deep golden-brown tones. These colors reflect the aging process in oak barrels and the richness of the flavors. Other associated colors might include dark brown and mahogany.
### 6. What is important to customers when buying Brandy?
Customers care about the origin of the Brandy, the aging time, the quality of the ingredients, the production method, and the brand. They also pay attention to the prestige of the product and the authenticity of the production.
### 7. What is not important to customers when buying Brandy?
For many customers, the price and packaging (unless it’s especially exclusive) may be less important than the quality and taste of the Brandy. The distillery name might be less significant if it isn’t tied to a particular reputation.
### 8. What do customers know about Swiss Brandy?
Swiss Brandy is still relatively unknown in many markets, but customers who are familiar with it appreciate the precision and quality of Swiss production. Swiss Brandy is assumed to be made with care and under strict quality standards.
### 9. What is Brandy Gran Reserva?
**Brandy Gran Reserva** is an even higher quality and longer-aged version of Brandy. Generally, a Gran Reserva is aged for at least 5 to 10 years or more in oak barrels. This extended aging process gives the Brandy an especially deep, complex flavor profile and often a darker, richer color. Gran Reserva is often regarded as the top-tier product within a Brandy range and appeals to discerning consumers who value quality, refinement, and a luxurious tasting experience.
The label “Gran Reserva” thus indicates the highest quality level for Brandies, similar to other spirits (like wine or whisky), where the aging time is a critical factor.
We age our Brandy Gran Reserva in the Solara way.
### 10. What emotions are associated with Brandy?
Brandy is often associated with luxury, relaxation, and comfort. It evokes feelings of tradition, elegance, and sophistication. Drinking Brandy is frequently seen as a moment of reflection and enjoyment.
### 11. How should Brandy be marketed?
Brandy should be marketed with a focus on its artisanal production, quality, and tradition. A narrative around the product, its aging, and origin can help create an emotional connection with the customer. The marketing should also emphasize the versatility of Brandy, whether consumed neat or in cocktails.
**Label design**:
The label should reflect the exclusivity of the product, with an elegant, minimalist design. The label should include information about the aging time, the use of oak barrels, and a brief story about the Brandy’s production.
we would like to have a modern look to the whole deisgn of the brandy
Customers that like Brandy
Switzerland
Distillery

```html
<!DOCTYPE html>
<html lang="en">
<head>
<meta charset="utf-8">
<title>Velmoris Brandy Gran Reserva – Label</title>
<link rel="stylesheet" href="https://fonts.googleapis.com/css2?family=Cinzel:wght@500;600&family=Cormorant+Garamond:wght@500;600&display=swap">
<style>
  :root {
    --backdrop: #d9d0c3;
    --label-brown: #3a1f16;
    --gold: #c9a04a;
    --gold-light: #e3c277;
    --cream: #efe6d6;
  }
  html, body {
    margin: 0;
    padding: 0;
    width: 1200px;
    height: 853px;
    overflow: hidden;
    background: var(--backdrop);
  }
  .label-artwork { display: block; width: 1200px; height: 853px; }
  .band { fill: var(--label-brown); }
  .gold-rule { stroke: var(--gold); stroke-width: 2.5; fill: none; }
  .gold-frame { stroke: var(--gold); fill: none; }
  .diamond-field { fill: var(--label-brown); }
  .title-text {
    font-family: "Cinzel", serif;
    font-weight: 600;
    fill: var(--gold-light);
  }
  .brand-name {
    font-family: "Cinzel", serif;
    font-weight: 600;
    fill: var(--cream);
    font-size: 32px;
  }
  .brand-sub {
    font-family: "Cinzel", serif;
    font-weight: 500;
    fill: var(--cream);
    font-size: 14px;
    letter-spacing: 1.5px;
  }
  .detail-text {
    font-family: "Cormorant Garamond", serif;
    font-weight: 500;
    fill: var(--cream);
    font-size: 13px;
  }
  .vintage { font-size: 16px; }
  .star { fill: var(--gold); }
</style>
</head>
<body>
<svg class="label-artwork" viewBox="0 0 1200 853" xmlns="http://www.w3.org/2000/svg">

  <!-- neck band -->
  <g class="neck-band">
    <rect class="band" x="500" y="38" width="200" height="58"/>
    <line class="gold-rule" x1="500" y1="46" x2="700" y2="46"/>
    <line class="gold-rule" x1="500" y1="88" x2="700" y2="88"/>
    <text class="title-text" x="600" y="75" text-anchor="middle" font-size="22">Gran Reserva</text>
  </g>

  <!-- main band -->
  <g class="main-band">
    <rect class="band" x="280" y="316" width="640" height="170"/>
    <line class="gold-rule" x1="280" y1="330" x2="920" y2="330"/>
    <line class="gold-rule" x1="280" y1="339" x2="920" y2="339"/>
    <line class="gold-rule" x1="280" y1="463" x2="920" y2="463"/>
    <line class="gold-rule" x1="280" y1="472" x2="920" y2="472"/>
    <g class="star-pair">
      <polygon class="star" points="298,394 300.4,399.5 306,400 301.7,403.6 303,409 298,406 293,409 294.3,403.6 290,400 295.6,399.5"/>
      <polygon class="star" points="312,396 313.8,400.2 318,400.5 314.8,403.2 315.8,407.3 312,405 308.2,407.3 309.2,403.2 306,400.5 310.2,400.2"/>
      <polygon class="star" points="902,394 904.4,399.5 910,400 905.7,403.6 907,409 902,406 897,409 898.3,403.6 894,400 899.6,399.5"/>
      <polygon class="star" points="888,396 889.8,400.2 894,400.5 890.8,403.2 891.8,407.3 888,405 884.2,407.3 885.2,403.2 882,400.5 886.2,400.2"/>
    </g>
  </g>

  <!-- central diamond -->
  <g class="diamond-label">
    <polygon class="diamond-field" points="600,132 868,400 600,668 332,400"/>
    <polygon class="gold-frame" stroke-width="3" points="600,148 852,400 600,652 348,400"/>
    <polygon class="gold-frame" stroke-width="1.5" points="600,160 840,400 600,640 360,400"/>

    <text class="brand-name" x="600" y="258" text-anchor="middle">Velmoris</text>
    <text class="brand-sub" x="600" y="282" text-anchor="middle">SWISS</text>
    <text class="brand-sub" x="600" y="299" text-anchor="middle">DISTILLERY</text>

    <text class="title-text" x="600" y="392" text-anchor="middle" font-size="44">Brandy</text>
    <text class="title-text" x="600" y="436" text-anchor="middle" font-size="40">Gran Reserva</text>

    <text class="detail-text" x="600" y="540" text-anchor="middle">Aged 5 years in oak barrels</text>
    <text class="detail-text" x="600" y="555" text-anchor="middle">Solera Method.</text>
    <text class="detail-text vintage" x="600" y="584" text-anchor="middle">2024</text>
  </g>

  <!-- lower band -->
  <g class="lower-band">
    <rect class="band" x="300" y="700" width="600" height="116"/>
    <line class="gold-rule" x1="300" y1="712" x2="900" y2="712"/>
    <line class="gold-rule" x1="300" y1="719" x2="900" y2="719"/>
    <line class="gold-rule" x1="300" y1="797" x2="900" y2="797"/>
    <line class="gold-rule" x1="300" y1="804" x2="900" y2="804"/>
    <text class="title-text" x="600" y="774" text-anchor="middle" font-size="46">Gran Reserva</text>
  </g>
</svg>
</body>
</html>
```